Letterhead for louvre roof company in NZ

I require a letter head design for a company called Slatwise Canopy.
I would like a footer to the letter head and possibly a water mark.
See attached logo.

```html
<!DOCTYPE html>
<html lang="en">
<head>
<meta charset="utf-8">
<title>Slatwise Canopy Letterhead</title>
<link rel="stylesheet" href="https://fonts.googleapis.com/css2?family=Lato:wght@400;700&family=Quicksand:wght@600&family=Yellowtail&display=swap">
<style>
  :root {
    --orange: #f0861f;
    --grey: #b7b7b7;
    --text: #4a4a4a;
    --paper: #ffffff;
  }
  * { box-sizing: border-box; margin: 0; padding: 0; }
  html, body { width: 942px; height: 1200px; overflow: hidden; background: var(--paper); }
  .sheet {
    position: relative;
    width: 942px;
    height: 1200px;
    background: var(--paper);
    font-family: "Lato", sans-serif;
    color: var(--text);
  }
  .brand {
    position: absolute;
    left: 78px;
    top: 24px;
    display: flex;
    flex-direction: column;
    align-items: flex-start;
    gap: 12px;
  }
  .brand-mark {
    width: 96px;
    height: 96px;
    background: var(--grey);
  }
  .brand-name {
    font-family: "Quicksand", sans-serif;
    font-weight: 600;
    font-size: 21px;
    color: var(--orange);
  }
  .contact {
    position: absolute;
    left: 705px;
    top: 60px;
    padding-left: 10px;
    border-left: 1px solid #c8c8c8;
    list-style: none;
    font-size: 13px;
    line-height: 23px;
    color: #333;
  }
  .contact li { display: flex; align-items: center; gap: 6px; }
  .contact svg { width: 11px; height: 11px; flex: none; }
  .letter {
    position: absolute;
    left: 81px;
    top: 336px;
    width: 783px;
  }
  .salutation {
    color: var(--orange);
    font-weight: 700;
    font-size: 17px;
    margin-bottom: 24px;
  }
  .letter p.body {
    font-size: 17.3px;
    line-height: 27px;
    text-align: justify;
    margin-bottom: 21px;
  }
  .closing { font-size: 21px; margin-top: 26px; }
  .signature {
    font-family: "Yellowtail", cursive;
    font-size: 38px;
    color: #333;
    margin-top: 4px;
  }
  .footer {
    position: absolute;
    left: 0;
    bottom: 0;
    width: 942px;
    height: 110px;
  }
  .footer svg { display: block; width: 942px; height: 110px; }
  .address {
    position: absolute;
    left: 85px;
    top: 66px;
    font-size: 13px;
    color: #fff;
  }
</style>
</head>
<body>
<div class="sheet">
  <header>
    <div class="brand">
      <div class="brand-mark"></div>
      <div class="brand-name">Slatwise Canopy</div>
    </div>
    <ul class="contact">
      <li><svg viewBox="0 0 12 12"><circle cx="6" cy="6" r="5.3" fill="none" stroke="#f0861f" stroke-width="1.2"/><path d="M4 3.3l1 1.4-.6.7c.4.9 1.1 1.6 2 2l.7-.6 1.4 1-.6 1C5.7 8.7 3.5 6.5 3.3 4z" fill="#f0861f"/></svg>021-555-0148</li>
      <li><svg viewBox="0 0 12 12"><circle cx="6" cy="6" r="5.3" fill="none" stroke="#f0861f" stroke-width="1.2"/><rect x="3.2" y="4" width="5.6" height="4" fill="none" stroke="#f0861f" stroke-width="0.9"/><path d="M3.2 4L6 6.2 8.8 4" fill="none" stroke="#f0861f" stroke-width="0.9"/></svg>info@slatwisecanopy.com</li>
      <li><svg viewBox="0 0 12 12"><circle cx="6" cy="6" r="5.3" fill="none" stroke="#f0861f" stroke-width="1.2"/><ellipse cx="6" cy="6" rx="2.2" ry="5.3" fill="none" stroke="#f0861f" stroke-width="0.9"/><path d="M0.8 6h10.4M1.8 3.5h8.4M1.8 8.5h8.4" stroke="#f0861f" stroke-width="0.9"/></svg>www.slatwisecanopy.com</li>
    </ul>
  </header>

  <main class="letter">
    <p class="salutation">Dear Mr. Lorem,</p>
    <p class="body">Lorem ipsum dolor sit amet, consectetuer adipiscing elit, sed diam nonummy nibh euismod tincidunt ut laoreet dolore magna aliquam erat volutpat. Ut wisi enim ad minim veniam, quis nostrud exerci tation ullamcorper suscipit lobortis nisl ut aliquip ex ea commodo consequat. Duis autem vel eum iriure dolor in hendiusto odio dignissim qui blandit praesent luptatum zzril delenit augue duis dolore te feugait nulla facilisi.</p>
    <p class="body">Lorem ipsum dolor sit amet, consectetuer adipiscing elit, sed diam nonummy nibh euismod tincidunt ut laoreet dolore magna aliquam erat volutpat. Ut wisi enim ad minim veniam, quis nostrud exerci tation ullamcorper suscipit lobortis nisl ut aliquip ex ea commodo consequat. Duis autem vel eum iriure dolor in hendiusto odio dignissim qui blandit praesent luptatum zzril delenit augue duis dolore te feugait nulla facilisi.</p>
    <p class="body">Lorem ipsum dolor sit amet, consectetuer adipiscing elit, sed diam nonummy nibh euismod tincidunt ut laoreet dolore magna aliquam erat volutpat. Ut wisi enim ad minim veniam, quis nostrud exerci tation ullamcorper suscipit lobortis nisl ut aliquip ex ea commodo consequat. Duis autem vel eum iriure dolor in hendiusto odio dignissim qui blandit praesent luptatum zzril delenit augue duis dolore te feugait nulla facilisi.</p>
    <p class="closing">Sincerely Your,</p>
    <p class="signature">Your Name</p>
  </main>

  <footer class="footer">
    <svg viewBox="0 0 942 110" preserveAspectRatio="none">
      <path d="M0 48 C220 10 430 18 600 70 C740 108 870 60 942 18 L942 110 L0 110 Z" fill="var(--orange)"/>
      <path d="M0 38 C220 0 430 8 600 60 C740 98 870 50 942 8" fill="none" stroke="var(--grey)" stroke-width="5"/>
      <path d="M520 44 C620 72 700 86 780 84 C850 82 900 66 942 50" fill="none" stroke="#fff" stroke-width="16"/>
      <path d="M520 46 C620 74 700 88 780 86 C850 84 900 68 942 52" fill="none" stroke="var(--grey)" stroke-width="6"/>
    </svg>
    <span class="address">Street Name, City Name, Zipcode-012345</span>
  </footer>
</div>
</body>
</html>
```